Creating a Label for the Wine "Marvessa"

Marvessa
As you know Marvessa is an imagined place or state of things in which everything is perfect. This wine reflects that. It is a high value wine and it is perfect. The dimensions shoulb be between 9c x 11,5 cm and 12cm x 8 cm

```html
<!DOCTYPE html>
<html lang="en">
<head>
<meta charset="utf-8">
<title>Marvessa – Wine Label</title>
<link href="https://fonts.googleapis.com/css2?family=Alike&family=Rye&display=swap" rel="stylesheet">
<style>
  :root {
    --parchment: #d9cbab;
    --gap-white: #ffffff;
    --bark-brown: #7d5c45;
    --wine-red: #9c3833;
    --ink: #5b4b3c;
    --bone: #c9a877;
    --petal-orange: #e98a32;
    --leaf-green: #4fa83c;
  }
  * { margin: 0; padding: 0; box-sizing: border-box; }
  html, body {
    width: 1200px;
    height: 796px;
    overflow: hidden;
    background: var(--gap-white);
  }
  .label {
    position: relative;
    width: 1200px;
    height: 796px;
    background: var(--gap-white);
    font-family: "Alike", Georgia, serif;
  }
  .brand-band {
    position: absolute;
    left: 0; top: 0;
    width: 1200px; height: 250px;
    background: var(--parchment);
    display: flex;
    align-items: center;
    justify-content: center;
    gap: 30px;
  }
  .brand-name {
    font-family: "Alike", Georgia, serif;
    font-weight: 400;
    font-size: 138px;
    line-height: 1;
    letter-spacing: 10px;
    color: var(--bark-brown);
    text-transform: uppercase;
  }
  .brand-mark {
    width: 34px; height: 34px;
    border-radius: 50%;
    background: var(--bark-brown);
  }
  .body-panel {
    position: absolute;
    left: 0; top: 280px;
    width: 1200px; height: 516px;
    background: var(--parchment);
    overflow: hidden;
  }
  .variety {
    position: absolute;
    left: 0; right: 0; top: 20px;
    text-align: center;
    font-family: "Rye", Georgia, serif;
    font-weight: 400;
    font-size: 64px;
    line-height: 1;
    color: var(--wine-red);
    letter-spacing: 2px;
  }
  .variety-ornament {
    position: absolute;
    left: 533px; top: 90px;
    width: 134px; height: 50px;
    border-radius: 25px;
    background: linear-gradient(90deg, rgba(201,168,119,0.25), rgba(201,168,119,0.75), rgba(201,168,119,0.25));
  }
  .spec {
    position: absolute;
    top: 140px;
    font-size: 27px;
    line-height: 32px;
    letter-spacing: 1px;
    color: var(--ink);
  }
  .spec--left { left: 44px; text-align: center; }
  .spec--right { right: 53px; text-align: right; }
  .flora {
    position: absolute;
    left: 0; bottom: 0;
    width: 1200px; height: 316px;
    background: linear-gradient(180deg,
      rgba(217,203,171,0) 0%,
      var(--petal-orange) 40%,
      var(--leaf-green) 100%);
  }
</style>
</head>
<body>
  <main class="label">
    <header class="brand-band">
      <span class="brand-name">Marvessa</span>
      <span class="brand-mark" aria-hidden="true"></span>
    </header>
    <section class="body-panel">
      <h1 class="variety">TAL</h1>
      <div class="variety-ornament" role="img" aria-label="Small decorative fish-bone ornament"></div>
      <p class="spec spec--left">Alcohol 12% By Volume<br>750 ml</p>
      <p class="spec spec--right">Lorem Ipsum<br>Dolor Sit Amet</p>
      <div class="flora" role="img" aria-label="Watercolour illustration of bird-of-paradise flowers with orange and blue petals among green leaves"></div>
    </section>
  </main>
</body>
</html>
```